Tessaway Website Redesign

We have a web site called tessaway.com that is all about education/information about legal marijuana. We're looking to significantly improve the modern-ness and look/feel of the web site - and to make it look like many of the best web sites out there today.

The task will be to come up with a better design for:
- The home page: http://tessaway.com/
- The logo (see the logo at the top of each page)
- The header and footer (for all the pages)
- The vaporizer page: http://tessaway.com/collections/vaporizer
- The store map page: http://tessaway.com/pages/shop-marijuana-in-colorado-state

The output of the project will be:
- screenshots of the designs and any images needed
- PSD file

Key requirements:
- Style needs to look fresh/modern
- Especially on the vaporizers page, the key things we want to drive is conversion - getting more people to interact with the page and actually click on the links to purchase vaporizers

Note I clarified that I don't need code (HTML or CSS) for the project. I just need the designs, including images and the PSD file. Thanks.

Industry/Entity Type

Education

Font styles to use
Sans Serif

Requirements
Must have
• Must look like a modern/clean/fresh looking website design.

```html
<!DOCTYPE html>
<html lang="en">
<head>
<meta charset="utf-8">
<title>Tessaway — Shop marijuana in style</title>
<link href="https://fonts.googleapis.com/css2?family=Open+Sans:wght@400;600;700;800&display=swap" rel="stylesheet">
<style>
:root{
  --green:#2ac951;
  --green-line:#8fe3a4;
  --mint:#a8f0bb;
  --grey-bg:#f4f4f4;
  --ink:#2b2b2b;
  --text:#555;
  --muted:#8a8a8a;
  --rule:#e2e2e2;
  --white:#fff;
}
*{margin:0;padding:0;box-sizing:border-box}
html,body{width:1200px;height:900px;overflow:hidden}
body{font-family:"Open Sans",Arial,sans-serif;color:var(--ink);background:var(--white);position:relative}

.site-header{position:absolute;left:0;top:0;width:1200px;height:73px;border-top:3px solid var(--green-line);border-bottom:1px solid var(--green-line)}
.brand{position:absolute;left:182px;top:10px;display:flex;align-items:center;gap:9px}
.brand-name{font-weight:800;font-size:46px;color:var(--green);letter-spacing:3.5px;line-height:50px}
.brand-tagline{font-size:12.5px;font-weight:600;color:#222;margin-top:4px}
.social{position:absolute;left:918px;top:8px;display:flex;gap:9px}
.social span{width:23px;height:23px;border-radius:50%;background:#c9c9c9}

.main-nav{position:absolute;left:0;top:73px;width:1200px;height:39px;border-bottom:1px solid var(--green-line)}
.main-nav ul{list-style:none;display:flex;gap:26px;position:absolute;left:182px;top:11px;font-size:12px;letter-spacing:.35px;font-weight:600;color:#333}

.hero{position:absolute;left:0;top:112px;width:1200px;height:173px;background:var(--green);text-align:center;color:var(--white)}
.hero h1{font-size:31px;letter-spacing:1.9px;font-weight:700;margin-top:27px;line-height:36px}
.hero p{font-size:14px;letter-spacing:.7px;margin-top:6px}
.search{position:absolute;left:309px;top:104px;width:599px;height:38px;background:var(--white);display:flex;align-items:center;padding-left:17px;gap:12px;color:#777;font-family:Arial,Helvetica,sans-serif;font-size:12.5px;text-align:left}

.features{position:absolute;left:0;top:285px;width:1200px;height:171px;background:var(--grey-bg)}
.feature{position:absolute;top:24px;width:298px;text-align:center}
.feature h2{font-size:19px;letter-spacing:1.2px;font-weight:600;margin-top:8px;color:#222}
.feature p{font-size:11.5px;letter-spacing:.6px;color:var(--text);line-height:14px;margin-top:9px}

.articles{position:absolute;left:182px;top:456px;width:604px;height:202px}
.articles h3{position:absolute;top:27px;font-size:13px;letter-spacing:1px;font-weight:600}
.articles .rule{position:absolute;left:118px;top:39px;width:486px;border-top:1px solid var(--rule)}
.articles .pager{position:absolute;left:580px;top:23px;font-size:14px;font-weight:700;letter-spacing:2px}
.article-list{position:absolute;list-style:none;top:50px}
.article-list li{display:flex;align-items:center;gap:18px;height:30px;font-size:11.5px;letter-spacing:.7px;color:#444;white-space:nowrap}

.policy{position:absolute;left:816px;top:484px;width:222px;height:161px;background:var(--mint);padding:17px 25px}
.policy h4{font-size:14.5px;letter-spacing:.8px;font-weight:600;color:#222}
.policy p{font-size:11px;letter-spacing:.35px;line-height:13.8px;margin-top:13px;color:#333}

.widgets{position:absolute;left:0;top:658px;width:1200px;height:190px;background:var(--grey-bg)}
.widget{position:absolute;top:30px;width:270px}
.widget h5{font-size:15.5px;letter-spacing:.5px;font-weight:600;color:#222}
.widget p{font-size:11px;letter-spacing:.35px;color:var(--text);line-height:14px;margin-top:13px}
.widget p+p{margin-top:8px}
.news{display:flex;gap:13px;margin-top:13px}
.news+.news{margin-top:17px}
.thumb{width:51px;height:36px;background:linear-gradient(#a9c3da,#7c8d7f 65%,#6b7a5a)}
.news strong{display:block;font-size:11px;letter-spacing:.2px;font-weight:700;color:#222}
.news small{display:block;font-size:9.5px;letter-spacing:.3px;color:var(--muted);margin-top:0}
.cats{list-style:none;margin-top:13px;font-size:11px;letter-spacing:.4px;color:#444}
.cats li{height:26.5px;display:flex;gap:11px}
.cats li::before{content:"›";color:#777}

.site-footer{position:absolute;left:0;top:848px;width:1200px;height:52px;background:var(--green);color:var(--white);font-size:10px}
.copyright{position:absolute;left:182px;top:20px;letter-spacing:.3px}
.footer-nav{position:absolute;right:162px;top:19px;display:flex;gap:14px;font-size:11px;letter-spacing:.3px}
.footer-nav i{font-style:normal;opacity:.6}
</style>
</head>
<body>

<header class="site-header">
  <div class="brand">
    <span class="brand-name">Tessaway</span>
    <span class="brand-tagline">Shop marijuana in style</span>
  </div>
  <div class="social" aria-label="Social links"><span></span><span></span><span></span><span></span></div>
</header>

<nav class="main-nav">
  <ul><li>Home</li><li>Blog &nbsp;+</li><li>Marijuana 101</li><li>Legal Marijuana</li><li>Vaporizers</li><li>Contact Us</li></ul>
</nav>

<section class="hero">
  <h1>Lorem ipsum dolor sit amet consectetur</h1>
  <p>Lorem Ipsum is simply dummy text of the printing and typesetting industry</p>
  <div class="search">
    <svg width="20" height="20" viewBox="0 0 20 20"><circle cx="8" cy="8" r="6" fill="none" stroke="#666" stroke-width="2.2"/><line x1="12.5" y1="12.5" x2="18" y2="18" stroke="#666" stroke-width="2.6" stroke-linecap="round"/></svg>
    <span>Search the knowledge base...</span>
  </div>
</section>

<section class="features">
  <div class="feature" style="left:161px">
    <svg width="50" height="48" viewBox="0 0 50 48"><path d="M6 3h26l12 12v28a3 3 0 0 1-3 3H6a3 3 0 0 1-3-3V6a3 3 0 0 1 3-3z" fill="none" stroke="#3a3a3a" stroke-width="3"/><path d="M32 3v12h12" fill="none" stroke="#3a3a3a" stroke-width="2.5"/><path d="M12 22h24M12 28h24M12 34h24" stroke="#3a3a3a" stroke-width="1.6"/></svg>
    <h2>Lorem ipsum</h2>
    <p>Lorem Ipsum is simply dummy text of the<br>printing and typesetting industry</p>
  </div>
  <div class="feature" style="left:459px">
    <svg width="50" height="48" viewBox="0 0 50 48"><path d="M6 3h26l12 12v28a3 3 0 0 1-3 3H6a3 3 0 0 1-3-3V6a3 3 0 0 1 3-3z" fill="none" stroke="#3a3a3a" stroke-width="3"/><path d="M32 3v12h12" fill="none" stroke="#3a3a3a" stroke-width="2.5"/><path d="M12 22h24M12 28h24M12 34h24" stroke="#3a3a3a" stroke-width="1.6"/></svg>
    <h2>Lorem ipsum</h2>
    <p>Lorem Ipsum is simply dummy text of the<br>printing and typesetting industry</p>
  </div>
  <div class="feature" style="left:758px">
    <svg width="50" height="48" viewBox="0 0 50 48"><path d="M6 3h26l12 12v28a3 3 0 0 1-3 3H6a3 3 0 0 1-3-3V6a3 3 0 0 1 3-3z" fill="none" stroke="#3a3a3a" stroke-width="3"/><path d="M32 3v12h12" fill="none" stroke="#3a3a3a" stroke-width="2.5"/><path d="M12 22h24M12 28h24M12 34h24" stroke="#3a3a3a" stroke-width="1.6"/></svg>
    <h2>Lorem ipsum</h2>
    <p>Lorem Ipsum is simply dummy text of the<br>printing and typesetting industry</p>
  </div>
</section>

<section class="articles">
  <h3>LOREM IPSUM</h3>
  <div class="rule"></div>
  <div class="pager">‹ ›</div>
  <ul class="article-list" style="left:0">
    <li><svg width="16" height="17" viewBox="0 0 16 17"><path d="M1.5 1h9l4 4v10.5h-13z" fill="none" stroke="#666"/><path d="M4 7h8M4 10h8M4 13h8" stroke="#666"/></svg>Ranking of vaporizers</li>
    <li><svg width="16" height="17" viewBox="0 0 16 17"><path d="M1.5 1h9l4 4v10.5h-13z" fill="none" stroke="#666"/><path d="M4 7h8M4 10h8M4 13h8" stroke="#666"/></svg>Map and ranking of Colorado Stores</li>
    <li><svg width="16" height="17" viewBox="0 0 16 17"><path d="M1.5 1h9l4 4v10.5h-13z" fill="none" stroke="#666"/><path d="M4 7h8M4 10h8M4 13h8" stroke="#666"/></svg>The 6 Best Ways to Store Your Weed</li>
    <li><svg width="16" height="17" viewBox="0 0 16 17"><path d="M1.5 1h9l4 4v10.5h-13z" fill="none" stroke="#666"/><path d="M4 7h8M4 10h8M4 13h8" stroke="#666"/></svg>Six Ways To Improve Your High</li>
  </ul>
  <ul class="article-list" style="left:311px">
    <li><svg width="16" height="17" viewBox="0 0 16 17"><path d="M1.5 1h9l4 4v10.5h-13z" fill="none" stroke="#666"/><path d="M4 7h8M4 10h8M4 13h8" stroke="#666"/></svg>How we all feel the first time we're high</li>
    <li><svg width="16" height="17" viewBox="0 0 16 17"><path d="M1.5 1h9l4 4v10.5h-13z" fill="none" stroke="#666"/><path d="M4 7h8M4 10h8M4 13h8" stroke="#666"/></svg>The Seven People You'll Meet Whilst High</li>
    <li><svg width="16" height="17" viewBox="0 0 16 17"><path d="M1.5 1h9l4 4v10.5h-13z" fill="none" stroke="#666"/><path d="M4 7h8M4 10h8M4 13h8" stroke="#666"/></svg>Top Ten Quotes About Weed</li>
    <li><svg width="16" height="17" viewBox="0 0 16 17"><path d="M1.5 1h9l4 4v10.5h-13z" fill="none" stroke="#666"/><path d="M4 7h8M4 10h8M4 13h8" stroke="#666"/></svg>The Craziest Drug Laws</li>
  </ul>
</section>

<aside class="policy">
  <h4>Support Policy</h4>
  <p>Lorem Ipsum is simply dummy text of the printing and typesetting industry. Lorem Ipsum has been the industry's standard dummy text ever since the 1500</p>
</aside>

<section class="widgets">
  <div class="widget" style="left:182px">
    <h5>About tessaway</h5>
    <p>Harborline Help is a responsive helpdesk Theme For PageCraft.</p>
    <p>Now you can have your own support center without paying monthly fees.</p>
  </div>
  <div class="widget" style="left:480px">
    <h5>Latest News</h5>
    <div class="news"><div class="thumb" role="img" aria-label="City skyline with a tower"></div><div><strong>Lorem ipsum dolor sit amet</strong><small>Aug 12, 2014</small></div></div>
    <div class="news"><div class="thumb" role="img" aria-label="Park with trees and city skyline" style="background:linear-gradient(#b7d3ea,#8aa57c 60%,#4f7a3c)"></div><div><strong>Lorem ipsum dolor sit amet</strong><small>Aug 12, 2014</small></div></div>
  </div>
  <div class="widget" style="left:778px">
    <h5>News Categories</h5>
    <ul class="cats"><li>Announcements</li><li>How-To</li><li>Strategy</li></ul>
  </div>
</section>

<footer class="site-footer">
  <div class="copyright">Copyright © 2014 Tessaway</div>
  <div class="footer-nav"><span>Home</span><i>/</i><span>Blog</span><i>/</i><span>Marijuana 101</span><i>/</i><span>Legal Marijuana</span><i>/</i><span>Vaporizer</span><i>/</i><span>Contact Us</span></div>
</footer>

</body>
</html>
```